Honey Label for 1kg square jar

We require premium looking honey label for 1kg packed in dark amber jar as shown in the image.
Brand is called :"Velmora Honey" - logo to be provided
We would like the following colours to be considered (white, gold and red)
We like to have some flowers and beehives on the background.
The label covers 3 sides of the square jar and were hoping to see render of the front side which should include the brand and also the words" 100% Premium Australian Honey"

Need extra days to review

```html
<!DOCTYPE html>
<html lang="en">
<head>
<meta charset="utf-8">
<title>Velmora Honey – Front Label</title>
<link rel="stylesheet" href="https://fonts.googleapis.com/css2?family=Kumbh+Sans:wght@500;700&family=Arvo:wght@700&family=Arimo:wght@400;700&display=swap">
<style>
  :root {
    --page: #ffffff;
    --cream: #f5f0e8;
    --brown: #3a2a22;
    --seal: #3d3129;
    --red: #4e1f1b;
    --gold-dark: #a8722c;
    --gold-light: #f0c760;
    --sketch: #dcc3a0;
    --sketch-soft: #ece0cc;
    --rule: #cdb89e;
  }
  * { margin: 0; padding: 0; box-sizing: border-box; }
  html, body { width: 1200px; height: 746px; overflow: hidden; background: var(--page); }
  .canvas { position: relative; width: 1200px; height: 746px; }

  .seal-strip {
    position: absolute; left: 561px; top: 90px; width: 77px; height: 120px;
    background: linear-gradient(180deg, var(--gold-dark), var(--gold-light) 70%, var(--gold-dark));
  }
  .label {
    position: absolute; left: 31px; top: 260px; width: 1138px; height: 335px;
    background: var(--cream);
  }
  .seal-mark {
    position: absolute; left: 498px; top: -64px; width: 142px; height: 142px;
    border-radius: 50%; background: var(--seal);
    border: 5px solid var(--gold-dark); z-index: 3;
  }
  .art { position: absolute; border-radius: 40%; }
  .art--hives { left: 284px; top: 0; width: 132px; height: 159px;
    background: radial-gradient(ellipse at 50% 50%, var(--sketch-soft), transparent 72%); }
  .art--flower { left: 52px; top: 193px; width: 210px; height: 77px; border-radius: 50% 50% 0 0;
    background: radial-gradient(ellipse at 50% 100%, var(--sketch-soft), transparent 70%); }
  .art--blossoms { left: 764px; top: 0; width: 200px; height: 69px; border-radius: 0 0 50% 50%;
    background: radial-gradient(ellipse at 50% 0%, var(--sketch-soft), transparent 72%); }
  .art--beehouse { left: 790px; top: 110px; width: 130px; height: 160px; border-radius: 8px;
    background: linear-gradient(180deg, var(--sketch-soft), rgba(236,224,204,0.3)); }
  .art--bee-a { left: 716px; top: 88px; width: 36px; height: 30px;
    background: radial-gradient(circle, var(--sketch), transparent 70%); }
  .art--bee-b { left: 387px; top: 175px; width: 42px; height: 36px;
    background: radial-gradient(circle, var(--sketch), transparent 70%); }

  .story {
    position: absolute; left: 53px; top: 32px; width: 200px;
    font: 500 13px/18.8px "Kumbh Sans", sans-serif; color: var(--brown); text-align: center;
  }

  .brand {
    position: absolute; left: 400px; top: 76px; width: 340px; text-align: center;
    font-family: "Kumbh Sans", sans-serif; font-weight: 700; color: var(--brown);
  }
  .brand__rule { height: 2px; background: var(--brown); margin: 0 28px; }
  .brand__name { display: block; font-size: 70px; line-height: 74px; letter-spacing: 1px; }
  .brand__sub { display: block; font-size: 48px; line-height: 52px; }

  .bands { position: absolute; left: 0; top: 230px; width: 1138px; height: 105px; }
  .tagline {
    position: absolute; left: 0; width: 1138px; top: 263px; text-align: center;
    font: 700 15.5px/20px "Arvo", serif; letter-spacing: 2px; color: var(--brown);
  }
  .net-weight {
    position: absolute; left: 0; width: 1138px; top: 306px; text-align: center;
    font: 500 16px/20px "Kumbh Sans", sans-serif; letter-spacing: 1px; color: var(--cream);
  }

  .nutrition {
    position: absolute; left: 907px; top: 20px; width: 196px; height: 230px;
    border: 1px solid var(--rule); background: var(--cream); padding: 8px 9px;
    font: 400 9.6px/13.2px "Arimo", sans-serif; color: var(--brown);
  }
  .nutrition h2 { font: 700 16.5px/19px "Arimo", sans-serif; }
  .nutrition b { font-weight: 700; }
  .nutrition .calories { font-size: 16px; font-weight: 700; }
  .nutrition .note { margin-top: 8px; font-size: 6.4px; line-height: 10px; }
</style>
</head>
<body>
<div class="canvas">
  <div class="seal-strip"></div>

  <section class="label" aria-label="Velmora Honey front label">
    <div class="art art--hives" role="img" aria-label="Sketch of hanging skep beehives"></div>
    <div class="art art--flower" role="img" aria-label="Sketch of a blooming flower"></div>
    <div class="art art--blossoms" role="img" aria-label="Sketch of blossoms and leaves"></div>
    <div class="art art--beehouse" role="img" aria-label="Sketch of a wooden beehive box"></div>
    <div class="art art--bee-a" role="img" aria-label="Small sketched bee"></div>
    <div class="art art--bee-b" role="img" aria-label="Small sketched bee"></div>

    <div class="seal-mark"></div>

    <p class="story">Lorem ipsum dolor sit amet, consectetuer adipiscing elit, sed diam nonummy nibh euismod tincidunt ut laoreet dolore magna aliquam erat volutpat. Ut wisi enim ad minim veniam, quis nostrud exerci tation ullamcorper</p>

    <h1 class="brand">
      <div class="brand__rule"></div>
      <span class="brand__name">VELMORA</span>
      <span class="brand__sub">Honey</span>
    </h1>

    <svg class="bands" viewBox="0 0 1138 105" aria-hidden="true">
      <defs>
        <linearGradient id="gold" x1="0" x2="1" y1="0" y2="0">
          <stop offset="0" stop-color="#a8722c"/>
          <stop offset="0.3" stop-color="#e9bd5c"/>
          <stop offset="0.5" stop-color="#c99a45"/>
          <stop offset="0.75" stop-color="#f0c760"/>
          <stop offset="1" stop-color="#a8722c"/>
        </linearGradient>
      </defs>
      <path d="M0 40 H330 C345 40 348 17 370 17 H768 C790 17 793 40 808 40 H1138 V68 H0 Z" fill="url(#gold)"/>
      <rect x="0" y="67" width="1138" height="38" fill="#4e1f1b"/>
    </svg>
    <p class="tagline">100% PREMIUM AUSTRALIAN HONEY</p>
    <p class="net-weight">Net Wt. 90 oz (255 g)</p>

    <aside class="nutrition">
      <h2>Nutrition Facts</h2>
      <p>Servings: 43, <b>Serv. size: 1 Tbsp (21g)</b>,</p>
      <p>Amount per serving: <b>Calories</b> <span class="calories">60,</span>
      <b>Total Fat</b> 0g (0% DV), Sat. Fat 0g (0% DV), Trans Fat 0g, <b>Cholest.</b> 0mg (0% DV), <b>Sodium</b> 0mg (0% DV), <b>Total Carb.</b> 17g (6% DV), Fiber 0g (0% DV), Total Sugars 17g (34% DV*), <b>Protein</b> 0g, Vit. D (0% DV), Calcium (0% DV), Iron (0% DV), Potas (0% DV).</p>
      <p class="note">* One serving adds 17g of sugar to your diet and<br>represents 34% of the<br>Daily Value for Added Sugars.</p>
    </aside>
  </section>
</div>
</body>
</html>
```